Need Website Design for Non-Profit Veteran Site

I am looking for a very talented creative website designer for a modern feel. I'll give a little bit of guidance around what I am looking for and then your creative juices should kick in and design away. I have already purchased the domain but will need hosting (at least temporarily) and the creative design work done.The website domain is militarydocs.orgI am looking to attract current and veteran military providers (doctors, nurse practitioners, physician assistants, etc) to join and signup for membership. They would pay a yearly fee to join. Would need membership categories $135 for Provider, $55 Student, $100 for Retired, and Organization (Organization would be broken down into Less than 100 ($200), 100-249 ($250), 250-499 ($300), 500-999 ($400), 1,000-2,999 ($500), and 3,000 ($700). Would need Benefit built out and would need to accept money through CoinLark and other means. Since it's a new organization just starting, would also need a Donate button to get people to donate if they want any amount they would like. The second part of the website is that once they join, they will have acess to a list of all other providers who have registered within the website (not exportable) so they can connect with one another. If they want to see contact information this will be included in their fee as a benefit to socialize with one another. As part of the website, there will be another Veteran's portal so veterans who would like to connect with a provider around a particular speciality can reach out and request help from the doctor writing a nexus letter or letter to support the veteran who is filing a claim with the OB. Veterans would pay a yearly sign-up fee of $30.00 and would need their membership benefits displayed. They would have access to a list of veterans in their region by state and distance, and can reach out to doctors to get their help. If a doctor and veteran agree, sharable inforamtion of medical hipaa documents can be exchanged via the website. The physician and veteran can negotiate a fee through the website only and share their details. This is a separate fee for this type of process between the provider and veteran. We will collect a $250 fee for admin on each of these and each project the veteran does with the provider will cost $450 (so essentially the doctor gets paid $450 and i get $250.00. This model could be changed over time as we start to test this out). A good example of 50% of what I'm looking for is something like the following website: https://www.qelvo.org/ It has some of the features but not all and my site should be more modernized to attract the veteran and military providers.

Target Market(s)

Current and retired military providers and veterans

Industry/Entity Type

Non Profit

Number of Pages Required

1 page

Requirements
Must have
• Military Design
• Modern Feel (Example templates for feel -https://tarnwickly.com/free-photoshop-psd-web-design-template/)
• Donation box
• Stuff mentioned in the description)
Nice to have
• Open to feedback
Should not have
• Open to feedback

```html
<!DOCTYPE html>
<html lang="en">
<head>
<meta charset="utf-8">
<title>brenfieldcare.org — Home</title>
<link rel="stylesheet" href="https://fonts.googleapis.com/css2?family=Arimo:wght@400;700&family=Roboto+Condensed:wght@700&display=swap">
<style>
:root{
  --navy:#030b5c;
  --navy-text:#0a1560;
  --ink:#0b2d52;
  --hero-top:#3c4874;
  --hero-bottom:#222a52;
  --hero-copy:#8e97b2;
  --accent:#0a8ad6;
  --card:#ffffff;
  --card-head:#d4e1ed;
  --field-line:#e3e6ea;
  --field-text:#16343a;
  --muted:#6c6f75;
  --white:#ffffff;
}
*{box-sizing:border-box;margin:0;padding:0}
html,body{width:1200px;height:1200px;overflow:hidden;background:var(--navy)}
body{font-family:"Arimo",Arial,sans-serif;position:relative}
.site-header{position:absolute;left:0;top:0;width:1200px;height:119px;background:var(--navy)}
.brand{position:absolute;left:128px;top:46px;color:var(--white);font-weight:700;font-size:20px}
.main-nav a{position:absolute;top:49px;color:var(--white);font-weight:700;font-size:19px;text-decoration:none}
.nav-home{left:649px}.nav-membership{left:784px}.nav-about{left:976px}
.hero{position:absolute;left:0;top:119px;width:1200px;height:549px;
  background:linear-gradient(180deg,var(--hero-top) 0%,#36416a 45%,var(--hero-bottom) 100%)}
.hero-title{position:absolute;left:118px;top:113px;width:520px;color:var(--white);font-size:43px;font-weight:700;line-height:45px}
.hero-copy{position:absolute;left:120px;top:225px;width:510px;color:var(--hero-copy);font-size:16.6px;font-weight:700;line-height:19.3px}
.btn{display:block;position:absolute;background:var(--accent);color:var(--white);font-size:19px;text-align:center;text-decoration:none}
.btn-donate{left:120px;top:348px;width:139px;height:43px;line-height:43px}
.signup-card{position:absolute;left:694px;top:168px;width:356px;height:452px;background:var(--card)}
.signup-title{position:absolute;left:24px;top:36px;font-family:"Roboto Condensed","Arial Narrow",sans-serif;font-size:27px;color:var(--ink)}
.signup-sub{position:absolute;left:24px;top:71px;font-size:13.5px;color:var(--muted)}
.field{position:absolute;left:22px;width:302px;height:44px;border:2px solid var(--field-line);padding-left:14px;line-height:40px;font-size:17px;color:var(--field-text)}
.field-name{top:115px}.field-email{top:190px}.field-confirm{top:260px}
.btn-continue{left:24px;top:342px;width:120px;height:43px;line-height:43px}
.info-card{position:absolute;top:722px;width:338px;height:424px;background:var(--card)}
.card-links{left:44px}.card-policy{left:428px}.card-news{left:818px}
.card-head{height:74px;background:var(--card-head);color:var(--navy-text);font-size:24px;padding:22px 0 0 20px}
.link-list{list-style:none;position:absolute;left:36px;top:83px}
.link-list li{position:relative;height:46px;padding-left:24px}
.link-list li::before{content:"";position:absolute;left:0;top:10px;width:16px;height:16px;background:var(--navy)}
.link-list a{color:var(--navy-text);font-size:19px;text-decoration:underline;text-underline-offset:3px}
.news-list{list-style:none}
.news-list li{position:absolute;left:20px;width:290px;padding-left:22px;font-size:12.6px;line-height:18px;color:var(--navy-text)}
.news-list li::before{content:"";position:absolute;left:0;top:2px;width:15px;height:15px;background:var(--navy)}
.n1{top:84px}.n2{top:148px}.n3{top:218px}.n4{top:278px}.n5{top:355px}
.card-news .n1{top:95px}.card-news .n2{top:159px}.card-news .n3{top:229px}.card-news .n4{top:289px}.card-news .n5{top:366px}
</style>
</head>
<body>
<header class="site-header">
  <div class="brand">brenfieldcare.org</div>
  <nav class="main-nav">
    <a class="nav-home" href="#">Home</a>
    <a class="nav-membership" href="#">Membership</a>
    <a class="nav-about" href="#">About Us</a>
  </nav>
</header>

<section class="hero" role="img" aria-label="Photo of a soldier in camouflage standing in a grassy field under a stormy sky, tinted dark blue">
  <h1 class="hero-title">This is a sample Home for brenfieldcare.org</h1>
  <p class="hero-copy">Lorem Ipsum is simply dummy text of the printing and typesetting industry. Lorem Ipsum has been the industry's standard dummy text ever since the 1500s, when an unknown printer took a galley of type and scrambled it to make a type specimen book.</p>
  <a class="btn btn-donate" href="#">Donation Box</a>
</section>

<form class="signup-card">
  <h2 class="signup-title">Membership</h2>
  <p class="signup-sub">Please complete the form</p>
  <div class="field field-name">*Name</div>
  <div class="field field-email">*Email Address</div>
  <div class="field field-confirm">*Confirm Email Address</div>
  <a class="btn btn-continue" href="#">Continue</a>
</form>

<section class="info-card card-links">
  <h3 class="card-head">Quick Links</h3>
  <ul class="link-list">
    <li><a href="#">Home</a></li>
    <li><a href="#">Membership</a></li>
    <li><a href="#">Renewal</a></li>
    <li><a href="#">About Us</a></li>
    <li><a href="#">Contact Us</a></li>
    <li><a href="#">Donation</a></li>
    <li><a href="#">Login</a></li>
  </ul>
</section>

<section class="info-card card-policy">
  <h3 class="card-head">Policy &amp; Practice News</h3>
  <ul class="news-list">
    <li class="n1">Lorem ipsum dolor sit amet, consectetur adipiscing elit, sed do eiusmod tempor incididunt ut labore et dolore magna.</li>
    <li class="n2">Lorem ipsum dolor sit amet, consectetur adipiscing elit, sed do eiusmod tempor incididunt ut labore et.</li>
    <li class="n3">Lorem ipsum dolor sit amet, consectetur adipiscing elit, sed do.</li>
    <li class="n4">Lorem ipsum dolor sit amet, consectetur adipiscing elit, sed do eiusmod tempor incididunt ut labore et dolore magna.</li>
    <li class="n5">Lorem ipsum dolor sit amet, consectetur adipiscing elit, sed do eiusmod tempor.</li>
  </ul>
</section>

<section class="info-card card-news">
  <h3 class="card-head">brenfieldcare.org News</h3>
  <ul class="news-list">
    <li class="n1">Lorem ipsum dolor sit amet, consectetur adipiscing elit, sed do eiusmod tempor incididunt ut labore et dolore magna.</li>
    <li class="n2">Lorem ipsum dolor sit amet, consectetur adipiscing elit, sed do eiusmod tempor incididunt ut labore et.</li>
    <li class="n3">Lorem ipsum dolor sit amet, consectetur adipiscing elit, sed do.</li>
    <li class="n4">Lorem ipsum dolor sit amet, consectetur adipiscing elit, sed do eiusmod tempor incididunt ut labore et dolore magna.</li>
    <li class="n5">Lorem ipsum dolor sit amet, consectetur adipiscing elit, sed do eiusmod tempor.</li>
  </ul>
</section>
</body>
</html>
```